Book Cover For Future Bestselling Entrepreneurship Book

The book is called:
Sell Levers: The Quick-Path Method to Earn Bonus Cash and Launch a Venture on Your Free Evenings

Somewhere on the cover, I'd like to experiment with a call-out that says "Featuring 300+ Apps and Marketplaces".

Author: Dale Farrow

The theme of the book is how to add your own personal "Sell Levers" on pre-existing marketplaces to reach a wide audience of buyers quickly. As far as artwork, I was thinking of a prominent literal "buy button" on the cover:
http://imgvault.eastzone4.cdn.plovermedia.com/dailyrivet.com/content/mcs/assets/v3/editorial/d/da/dd4e7a21-91fa-42b3-bc17-5e2a9f07c3d1/7a2b91c4de3f5.image.jpg

(doesn't have to be blue or look like that, could be an more "online" looking button.)

Take a look at some of the current bestselling business books:
https://www.shopvelt.com/Top-Sellers-Reader-Shop-Commerce-Finance/tops/digital-text/298417035/ref=tp_bs_nav_rshop_2_298410022#1

I like:
https://www.shopvelt.com/Week-Venture-Study-Before-Opening-ebook/dp/X44QLMRT2K/ref=tp_bs_298417035_75
https://www.shopvelt.com/Craft-Labor-Tested-Finding-Calling-ebook/dp/X44RJNDW7P/ref=tp_bs_298417035_18

Main criteria is something, clean and professional that still looks good in thumbnail form. If the files are delivered in a format I can edit, that's a big bonus because I'll need to make a square version for the audiobook and front/spine/back-cover for the paperback.

Dimensions 3000x4800, 300dpi

Target Market(s)

Aspiring entrepreneurs, people who want to make or need to money outside of a traditional job.

Industry/Entity Type

Small Business

Font styles to use
Sans Serif

Requirements
Must have
• Prominent Sell Levers text and a large button graphic
Nice to have
• A callout that says "Featuring 300+ Apps and Marketplaces"

```html
<!DOCTYPE html>
<html lang="en">
<head>
<meta charset="utf-8">
<title>Sell Levers – Book Cover</title>
<link rel="stylesheet" href="https://fonts.googleapis.com/css2?family=Russo+One&family=Roboto:ital,wght@0,400;0,700;0,900;1,900&display=swap">
<style>
  :root {
    --sky: #3fa9f0;
    --sky-deep: #1f86d6;
    --sky-light: #8fd0fb;
    --ink: #111111;
    --paper: #ffffff;
    --paper-shade: #e4e6e8;
    --rule: #2aa6ee;
  }
  html, body {
    margin: 0;
    padding: 0;
    width: 930px;
    height: 1200px;
    overflow: hidden;
    background: var(--paper);
  }
  .cover {
    position: relative;
    width: 930px;
    height: 1200px;
    overflow: hidden;
    background: radial-gradient(ellipse at 50% 40%, var(--paper) 45%, var(--paper-shade) 100%);
    font-family: "Roboto", Arial, sans-serif;
    color: var(--ink);
  }
  .title {
    position: absolute;
    top: 180px;
    left: 0;
    width: 100%;
    margin: 0;
    text-align: center;
    font-family: "Russo One", "Arial Black", sans-serif;
    font-weight: 400;
    font-size: 96px;
    letter-spacing: 4px;
    line-height: 1;
    background: linear-gradient(180deg, var(--sky-light) 0%, var(--sky) 45%, var(--sky-deep) 100%);
    -webkit-background-clip: text;
    background-clip: text;
    color: transparent;
  }
  .subtitle {
    position: absolute;
    top: 305px;
    left: 0;
    width: 100%;
    margin: 0;
    text-align: center;
    text-transform: uppercase;
    font-size: 42px;
    line-height: 1.22;
    font-weight: 400;
  }
  .subtitle .line { display: block; }
  .subtitle .strong { font-weight: 900; font-style: italic; }
  .subtitle .joiner {
    display: flex;
    align-items: flex-end;
    justify-content: center;
    gap: 22px;
    font-size: 32px;
    margin: 4px 0 6px;
  }
  .subtitle .joiner::before,
  .subtitle .joiner::after {
    content: "";
    width: 250px;
    height: 4px;
    background: var(--rule);
    margin-bottom: 4px;
  }
  .subtitle .small { font-size: 38px; }
  .button-art {
    position: absolute;
    left: 200px;
    top: 660px;
    width: 530px;
    height: 300px;
    border-radius: 36px;
    background: linear-gradient(180deg, #9fd6f8 0%, var(--sky) 55%, var(--sky-deep) 100%);
  }
  .author {
    position: absolute;
    top: 1010px;
    left: 0;
    width: 100%;
    margin: 0;
    text-align: center;
    font-weight: 900;
    font-size: 60px;
    line-height: 1;
    letter-spacing: 18px;
  }
  .callout {
    position: absolute;
    bottom: 0;
    left: 0;
    width: 100%;
    height: 74px;
    margin: 0;
    background: var(--ink);
    color: var(--paper);
    display: flex;
    align-items: center;
    justify-content: center;
    font-weight: 700;
    font-size: 28px;
    letter-spacing: 1px;
    text-transform: uppercase;
  }
  .callout .accent { color: var(--sky); margin: 0 0.3em; }
</style>
</head>
<body>
<main class="cover">
  <h1 class="title">SELL LEVERS:</h1>

  <p class="subtitle">
    <span class="line">The <span class="strong">Quick-Path Method</span> to</span>
    <span class="line strong">Earn Bonus Cash</span>
    <span class="line joiner">And</span>
    <span class="line strong">Launch a Venture</span>
    <span class="line small">On Your Free Evenings</span>
  </p>

  <div class="button-art" role="img" aria-label="Illustration of a large blue online buy button with a pointer cursor clicking it"></div>

  <h2 class="author">DALE FARROW</h2>

  <p class="callout">Featuring <span class="accent">300+ Apps</span> and <span class="accent">Marketplaces</span></p>
</main>
</body>
</html>
```